Covid19 Poster for workplaces

Create a poster on how to protect yourself from Corona virus at work.
We are a Staffwell Co company. We have just re-branded so we need to fit in with our brand. We like clean and fresh, slightly amusing is ok if it will draw attention but it's an important topic. A4 and A3 please.

Content:

Headline: Lower the risk of COVID 19 in the workplace.

BE WELL

Bring your own cup - don’t share cups and food.
Elbow tap instead of handshakes and kisses
Wash your hands often - with soap.
Elbow or tissues when you cough or sneeze then straight in the bin
Leave your face alone after touching shared surfaces
Leave your bugs at home if you’re feeling unwell.

Call health line if you have a cough, a high temperature and shortness of breath. 0800 472 9160

Based on recommendations from ZPK and QLN

Target Market(s)

Employees - so anyone

Other font styles liked:
• Use the closest font to the brand documents

Requirements
Should not have
• Clip art

```html
<!DOCTYPE html>
<html lang="en">
<head>
<meta charset="utf-8">
<title>COVID-19 Workplace Poster</title>
<link href="https://fonts.googleapis.com/css2?family=Arimo:wght@400;700&display=swap" rel="stylesheet">
<style>
  :root {
    --backdrop: #231f20;
    --paper: #ffffff;
    --teal: #1fa9b4;
    --teal-dark: #17869a;
    --ink: #111111;
    --photo-a: #2b3a4a;
    --photo-b: #3d6f8f;
  }
  * { margin: 0; padding: 0; box-sizing: border-box; }
  html, body { width: 1200px; height: 1200px; overflow: hidden; }
  body { background: var(--backdrop); font-family: "Arimo", Arial, sans-serif; position: relative; }

  .poster { position: absolute; left: 251px; top: 79px; width: 745px; height: 1031px; background: var(--paper); }

  .hero { position: absolute; left: 17px; top: 19px; width: 709px; height: 532px; background: var(--teal); }
  .hero-frame { position: absolute; left: 25px; top: 30px; width: 665px; height: 490px; border: 3px solid var(--paper); }

  .hero-title { position: absolute; left: 0; right: 0; top: 62px; color: var(--paper);
    font-weight: 700; font-size: 92px; line-height: 1; letter-spacing: -1px;
    display: flex; justify-content: center; align-items: center; }
  .virus-o { display: inline-block; width: 70px; height: 70px; border-radius: 50%; background: var(--paper); margin: 0 2px; position: relative; }
  .virus-o .virus { position: absolute; inset: 8px; border-radius: 50%; background: var(--teal-dark); }

  .hero-sub { position: absolute; left: 0; right: 0; top: 167px; text-align: center; color: var(--paper);
    font-weight: 700; font-size: 28px; line-height: 32px; }

  .hero-photo { position: absolute; left: 152px; top: 252px; width: 420px; height: 225px; border-radius: 110px;
    background: linear-gradient(120deg, var(--photo-a), var(--photo-b)); }

  .hero-tagline { position: absolute; left: 0; right: 0; top: 484px; text-align: center; color: var(--paper); font-size: 19px; letter-spacing: -0.3px; }
  .hero-tagline strong { font-weight: 700; }

  .tips { position: absolute; left: 43px; top: 566px; right: 40px; list-style: none; }
  .tip { position: absolute; left: 0; width: 100%; height: 46px; }
  .tip-badge { position: absolute; left: 10px; top: 0; width: 44px; height: 44px; border-radius: 50%; background: var(--teal-dark);
    color: var(--paper); font-weight: 700; font-size: 22px; line-height: 44px; text-align: center; }
  .tip-title { position: absolute; left: 94px; top: 1px; color: var(--teal); font-weight: 700; font-size: 21px; white-space: nowrap; letter-spacing: -0.3px; }
  .tip-text { position: absolute; left: 94px; top: 27px; width: 570px; color: var(--ink); font-size: 12.5px; line-height: 14px; white-space: nowrap; letter-spacing: -0.2px; }
  .tip-1 { top: 0; } .tip-2 { top: 50px; } .tip-3 { top: 100px; }
  .tip-4 { top: 150px; } .tip-5 { top: 200px; } .tip-6 { top: 250px; }

  .healthline { position: absolute; left: 53px; right: 40px; top: 870px; color: var(--ink); font-size: 12.5px; line-height: 16px; letter-spacing: -0.2px; }
  .healthline strong { color: var(--teal-dark); font-weight: 700; font-size: 14px; }

  .divider-dots { position: absolute; left: 0; right: 0; top: 916px; border-top: 3px dotted var(--teal); }

  .footer { position: absolute; left: 0; right: 0; top: 936px; height: 55px; }
  .brand { position: absolute; left: 46px; top: 6px; display: flex; align-items: center; gap: 12px; }
  .brand-dot { width: 40px; height: 40px; border-radius: 50%; background: var(--teal); }
  .brand-name { color: var(--ink); font-weight: 700; font-size: 22px; line-height: 20px; width: 120px; }
  .rule { position: absolute; top: 3px; width: 2px; height: 48px; background: var(--ink); }
  .rule-1 { left: 251px; } .rule-2 { left: 441px; }
  .phone { position: absolute; left: 268px; top: 12px; display: flex; align-items: center; gap: 9px; font-weight: 700; font-size: 25px; color: var(--ink); }
  .web { position: absolute; left: 455px; top: 17px; display: flex; align-items: center; gap: 7px; font-weight: 700; font-size: 13.5px; color: var(--ink); }
</style>
</head>
<body>
  <main class="poster">
    <section class="hero">
      <div class="hero-frame"></div>
      <h1 class="hero-title">C<span class="virus-o"><span class="virus" role="img" aria-label="Coronavirus particle illustration"></span></span>VID-19</h1>
      <h2 class="hero-sub">LOWER THE RISK OF COVID-19<br>IN THE WORKPLACE</h2>
      <div class="hero-photo" role="img" aria-label="Photo of smiling colleagues in an office"></div>
      <p class="hero-tagline"><strong>BE WELL.</strong> People work better, When they feel good. Simple.</p>
    </section>

    <ul class="tips">
      <li class="tip tip-1">
        <span class="tip-badge">B</span>
        <h3 class="tip-title">Bring your own cup</h3>
        <p class="tip-text">Don’t share cups and food.</p>
      </li>
      <li class="tip tip-2">
        <span class="tip-badge">E</span>
        <h3 class="tip-title">Elbow tap</h3>
        <p class="tip-text">Elbow tap instead of handshakes and kisses.</p>
      </li>
      <li class="tip tip-3">
        <span class="tip-badge">W</span>
        <h3 class="tip-title">Wash your hands often</h3>
        <p class="tip-text">Wash your hands often, with soap.</p>
      </li>
      <li class="tip tip-4">
        <span class="tip-badge">E</span>
        <h3 class="tip-title">Elbow or tissues</h3>
        <p class="tip-text">Use your elbow or tissues when you cough or sneeze, then straight in the bin.</p>
      </li>
      <li class="tip tip-5">
        <span class="tip-badge">L</span>
        <h3 class="tip-title">Leave your face alone</h3>
        <p class="tip-text">Leave your face alone after touching shared surfaces.</p>
      </li>
      <li class="tip tip-6">
        <span class="tip-badge">L</span>
        <h3 class="tip-title">Leave your bugs at home</h3>
        <p class="tip-text">Leave your bugs at home if you’re feeling unwell.</p>
      </li>
    </ul>

    <p class="healthline">Call health line if you have a cough, a high temperature and shortness of breath. <strong>0800 472 9160</strong><br>Based on recommendations from ZPK and QLN.</p>

    <div class="divider-dots"></div>

    <footer class="footer">
      <div class="brand"><span class="brand-dot"></span><span class="brand-name">Staffwell Co</span></div>
      <span class="rule rule-1"></span>
      <div class="phone">
        <svg width="20" height="20" viewBox="0 0 20 20" aria-hidden="true"><rect x="1" y="1" width="18" height="18" rx="4" fill="#111"/><path d="M7 5c-1 0-2 1-1.6 2.6.8 3 3 5.3 6 6.3 1.6.5 2.6-.6 2.6-1.6l-2-1-1 1c-1.4-.6-2.7-1.9-3.3-3.3l1-1z" fill="#fff"/></svg>
        <span>035820917</span>
      </div>
      <span class="rule rule-2"></span>
      <div class="web">
        <svg width="18" height="18" viewBox="0 0 18 18" aria-hidden="true" fill="none" stroke="#111" stroke-width="1.3"><circle cx="9" cy="9" r="7.5"/><ellipse cx="9" cy="9" rx="3.2" ry="7.5"/><path d="M1.5 9h15M2.7 5h12.6M2.7 13h12.6"/></svg>
        <span>www.staffwellco.co.nz</span>
      </div>
    </footer>
  </main>
</body>
</html>
```